Luxury Resort Complex needs a Power Point Shell

Working in our primary color palate (pms colors can be provided and seen on our web site www.thelumenvale.com) design a title page, chapter page, and three slide page templates that include our logo either screened into the background or somewhere on the page which we can use for internal and external power point presentations.

Target Market(s)

Internal and External constituents

Industry/Entity Type

Hotel

```html
<!DOCTYPE html>
<html lang="en">
<head>
<meta charset="utf-8">
<title>Drink &amp; Dine — The Lumen Vale</title>
<link rel="stylesheet" href="https://fonts.googleapis.com/css2?family=Tenor+Sans&display=swap">
<style>
  :root {
    --paper: #ffffff;
    --ink: #5a5b5d;
    --navy: #1b2a47;
    --blush: #e8a09f;
  }
  html, body {
    margin: 0;
    padding: 0;
    width: 1200px;
    height: 643px;
    overflow: hidden;
    background: var(--paper);
  }
  .slide {
    position: relative;
    width: 1200px;
    height: 643px;
    overflow: hidden;
    background: var(--paper);
    color: var(--ink);
    font-family: "Tenor Sans", "Optima", sans-serif;
  }
  .slide-title {
    position: absolute;
    top: 78px;
    left: 0;
    width: 1256px;
    margin: 0;
    text-align: center;
    font-weight: 400;
    font-size: 30px;
    letter-spacing: 0.3px;
  }
  .intro {
    position: absolute;
    top: 145px;
    left: 78px;
    width: 1034px;
    margin: 0;
    text-align: center;
    font-size: 20.5px;
    line-height: 35.7px;
  }
  .column {
    position: absolute;
    width: 482px;
    font-size: 20.5px;
    line-height: 35.7px;
    text-align: justify;
    hyphens: auto;
  }
  .column p { margin: 0; }
  .column-left { top: 259px; left: 81px; }
  .column-right { top: 256px; left: 630px; }
  .accent-band {
    position: absolute;
    left: 3px;
    top: 582px;
    width: 828px;
    height: 14px;
    background: var(--blush);
  }
  .brand-name {
    position: absolute;
    left: 846px;
    top: 568px;
    margin: 0;
    color: var(--navy);
    font-family: "Tenor Sans", "Optima", sans-serif;
    font-weight: 400;
    font-size: 33px;
    line-height: 40px;
    white-space: nowrap;
  }
</style>
</head>
<body>
  <main class="slide">
    <h1 class="slide-title">Drink &amp; Dine</h1>

    <p class="intro">This space is reserved for programe information and any other descriptions etc. This space is reserved for programe information and any other descriptions etc. This space is reserved for programe information.</p>

    <div class="column column-left" lang="en">
      <p>This space is reserved for programe information and any other descriptions etc. This space is reserved for programe information and any other descriptions etc. This space is reserved for programe information.</p>
      <p>Information and any other descriptions etc. This space is reserved for programe information and any other descriptions etc.&nbsp; This space is reserved</p>
    </div>

    <div class="column column-right" lang="en">
      <p>for programe information and any other descriptions etc.This space is reserved for programe information and any other descriptions etc.This space is reserved for programe information.</p>
    </div>

    <div class="accent-band"></div>

    <p class="brand-name">The Lumen Vale</p>
  </main>
</body>
</html>
```